Simple Lawyer Business Card Design Project with gold foil

Looking for a double sided business card. I would like to incorporate two of the images I attached onto the card- a monogram M in a circle and the legal image.
I also added image # 2 as a possibility of how to incorporate both images and for the layout of the information.

Back Side: This side of card will be one version in maroon and one version in white. The logo/vector on back side of card with business name Calloway Legal Group. Shield/Vector should be placed above the Calloway Legal Group lettering in a gold foil press. Please use colors of attachment #3.

Front Side: front of card will be white. front of card could have the monogram M in circle on background (where the lightened scales are on the sample card), with company information over it- Calloway Legal Group. *please delete the crown image above the M* Would like to see the monogram logo in gold -Calloway Legal Group will be in gold foil. Everything on left side should be black font.

Dorinda Featherstone, Esq.
Principal Attorney
Address: 17 Harrow Crest Ave. Suite 812 Woodcliff Lake,
NJ 07912
Phone: 201-739-5186
Fax: 201-627-9340
Email: dfeatherstone@qorvantlaw.com
www.qorvantlaw.com

Industry/Entity Type

Lawyer

Contact Information for Business Card

Dorinda Featherstone, Esq.
Principal Attorney
Address: 17 Harrow Crest Ave. Suite 812 Brenwick Falls 07912
Phone: 201-739-5186
Fax: 201-627-9340
www.qorvantlaw.com

Font styles to use
Serif
Other font styles liked:
• fonts on samples

Colors
ffffff

Requirements
Must have
• - The final files must conform w/:
• - https://www.zelvapress.com/velvet-w-pressed-sheen-business-cards
• - https://www.zelvapress.com/template-files/business-cards/3.5x2.zip
• - https://www.vidrowlo.com/watch?v=Qk2TzR7pWnA#action=share
• - we would ask that you upload single page .pdf files only.
• - we recommend a Rich Black value of C=60, M=40, Y=40, K=100
• - Foil mask files are set up just like our Spot UV mask files. The file will only be black and white. The black areas will show where you want the foil placed. White will show areas where you do not want the foil. When ordering a Foil Stamp job with Spot UV, you must provide separate mask files for the Foil (foil mask) and Spot UV (spuv mask). Up to Six files would need to be provided.
• - When using Foil, please keep in mind that Foil and UV can not overlap and we recommend avoiding the use of small/fine text or fonts for foil objects. For best results, please be sure foil coverage is less than 50% of the artwork area.
• - It’s also important to note that there may be up to 1/16" shift on the placement of the foil. Keep this in mind if you are trying to align foil with other printed artwork.
Should not have
• don't want anything cluttered

```html
<!DOCTYPE html>
<html lang="en">
<head>
<meta charset="utf-8">
<title>Calloway Legal Group — Business Card</title>
<link href="https://fonts.googleapis.com/css2?family=Rokkitt:wght@500&family=Source+Sans+3:wght@400&display=swap" rel="stylesheet">
<style>
  :root{
    --backdrop:#b88c5c;
    --card:#ffffff;
    --ink:#3a3a3a;
    --gold:#b3923f;
    --ring:#e3e3e3;
  }
  *{margin:0;padding:0;box-sizing:border-box}
  html,body{width:1200px;height:1200px;overflow:hidden;background:var(--backdrop)}
  .card{
    position:absolute;left:286px;width:628px;height:390px;
    background:var(--card);
    box-shadow:14px 18px 30px rgba(0,0,0,.28);
  }
  .card--front{top:150px}
  .card--back{top:681px}

  .front__ring{position:absolute;left:294px;top:31px;width:328px;height:328px}
  .attorney{position:absolute;left:26px;top:42px;font-family:"Rokkitt",serif;font-weight:500;color:var(--ink)}
  .attorney__name{font-size:20px;line-height:24px;letter-spacing:.2px;white-space:nowrap}
  .attorney__title{font-size:17px;line-height:22px;letter-spacing:.6px}

  .contact{position:absolute;left:26px;top:176px;list-style:none;font-family:"Source Sans 3",sans-serif;font-size:16px;color:var(--ink)}
  .contact li{position:relative;padding-left:30px;line-height:22px}
  .contact svg{position:absolute;left:0;top:5px;width:13px;height:13px}
  .contact .gap{margin-top:13px}
  .contact .gap-sm{margin-top:5px}

  .firm-name{font-family:"Rokkitt",serif;font-weight:500;color:var(--gold);text-align:center;letter-spacing:2px}
  .firm-name--front{position:absolute;left:294px;width:328px;top:166px;font-size:25px;line-height:30px}
  .firm-name--back{position:absolute;left:0;width:628px;top:240px;font-size:36px;line-height:42px}

  .back__badge{position:absolute;left:231px;top:65px;width:164px;height:164px}
</style>
</head>
<body>
  <section class="card card--front" aria-label="Card front">
    <svg class="front__ring" viewBox="0 0 328 328" aria-hidden="true">
      <circle cx="164" cy="164" r="156" fill="none" stroke="var(--ring)" stroke-width="8"/>
    </svg>
    <div class="firm-name firm-name--front">CALLOWAY<br>LEGAL GROUP</div>

    <header class="attorney">
      <div class="attorney__name">DORINDA FEATHERSTONE, ESQ.</div>
      <div class="attorney__title">ATTORNEY AT LAW</div>
    </header>

    <ul class="contact">
      <li>
        <svg viewBox="0 0 12 12"><path d="M6 0.5a3.6 3.6 0 0 0-3.6 3.6C2.4 7 6 11.5 6 11.5S9.6 7 9.6 4.1A3.6 3.6 0 0 0 6 .5z" fill="none" stroke="var(--gold)" stroke-width="1.3"/><circle cx="6" cy="4.1" r="1.2" fill="var(--gold)"/></svg>
        17 Harrow Crest Ave. Suite 812<br>Brenwick Falls 07912
      </li>
      <li class="gap">
        <svg viewBox="0 0 12 12"><path d="M1 4c0-2 10-2 10 0v1H8V3.8H4V5H1z" fill="var(--gold)"/><rect x="2.5" y="6" width="7" height="4.5" rx="1" fill="var(--gold)"/></svg>
        201-739-5186
      </li>
      <li class="gap-sm">
        <svg viewBox="0 0 12 12"><rect x="1" y="5" width="10" height="6" fill="var(--gold)"/><rect x="3.5" y="1" width="5" height="4" fill="none" stroke="var(--gold)" stroke-width="1.2"/></svg>
        201-627-9340
      </li>
      <li class="gap">
        <svg viewBox="0 0 12 12"><rect x="0.8" y="2.5" width="10.4" height="7" fill="none" stroke="var(--gold)" stroke-width="1.2"/><path d="M1 3l5 3.5L11 3" fill="none" stroke="var(--gold)" stroke-width="1.2"/></svg>
        dfeatherstone@qorvantlaw.com
      </li>
      <li class="gap-sm">
        <svg viewBox="0 0 12 12" fill="none" stroke="#9a9a9a" stroke-width="0.9"><circle cx="6" cy="6" r="5"/><ellipse cx="6" cy="6" rx="2.2" ry="5"/><path d="M1 6h10M2 3.3h8M2 8.7h8"/></svg>
        www.qorvantlaw.com
      </li>
    </ul>
  </section>

  <section class="card card--back" aria-label="Card back">
    <svg class="back__badge" viewBox="0 0 164 164" aria-hidden="true">
      <circle cx="82" cy="82" r="82" fill="var(--gold)"/>
    </svg>
    <div class="firm-name firm-name--back">CALLOWAY<br>LEGAL GROUP</div>
  </section>
</body>
</html>
```